Coming Soon HTML5 Animated landing page

We need a landing page showing vape movement and our logo (With some discreet movement) stating "Fire Prices on Premium E-Juices Vaping soon" with a contemporary countdown with the colors of our logo. A Countdown will be nice (A contemporary one, Bold) providing all required files. Java Script, CSS, Graphics, Videos and of course HTML....

Target Market(s)

Male/Female 21 - 40 Years Old, Vape Lovers and E-Cigarrette consumers

Coding

Coded - Design and coding required

Number of Pages Required

2 page

Font styles to use
Sans Serif
Other font styles liked:
• Look at our logo

Colors
f37122
ffc214

Requirements
Must have
• A cool HTML5 animation, Vapor movement or exhaled. A configurable count down.
Nice to have
• Would love to see our logo forming
Should not have
• Corny and old concepts...

```html
<!DOCTYPE html>
<html lang="en">
<head>
<meta charset="utf-8">
<title>Embermist – Vaping Soon</title>
<link rel="stylesheet" href="https://fonts.googleapis.com/css2?family=Roboto:wght@500;700;900&family=Raleway:wght@500;600;700&display=swap">
<style>
  :root {
    --orange: #f37122;
    --yellow: #ffc214;
    --white: #ffffff;
    --forest-dark: #0f1a10;
    --forest-mid: #24331f;
    --forest-light: #3d4a35;
    --track: #3a352e;
    --ink: #1a1a1a;
  }
  * { margin: 0; padding: 0; box-sizing: border-box; }
  html, body { width: 1200px; height: 800px; overflow: hidden; background: var(--forest-dark); }
  .page {
    position: relative;
    width: 1200px;
    height: 800px;
    overflow: hidden;
    font-family: "Raleway", sans-serif;
    color: var(--white);
  }
  .hero-photo {
    position: absolute; inset: 0;
    background:
      radial-gradient(ellipse 18% 30% at 50% 32%, rgba(120,125,110,0.55), transparent 70%),
      linear-gradient(180deg, transparent 55%, rgba(58,53,46,0.6) 100%),
      radial-gradient(ellipse 60% 90% at 50% 100%, var(--forest-light), transparent 70%),
      linear-gradient(90deg, var(--forest-mid) 0%, var(--forest-dark) 45%, var(--forest-dark) 55%, var(--forest-mid) 100%);
  }
  .hero-photo::after {
    content: ""; position: absolute; inset: 0; background: rgba(0,0,0,0.25);
  }

  .brand {
    position: absolute; left: 32px; top: 64px;
    display: flex; align-items: center; gap: 10px;
  }
  .brand-dot { width: 14px; height: 14px; border-radius: 50%; background: var(--orange); }
  .brand-name {
    font-family: "Roboto", sans-serif; font-weight: 700;
    font-size: 34px; letter-spacing: 1px; color: var(--orange);
  }

  .main-nav {
    position: absolute; top: 66px; right: 35px;
    display: flex; align-items: center; gap: 40px;
    font-size: 16px; font-weight: 600;
  }
  .main-nav a { color: var(--white); text-decoration: none; }
  .main-nav .nav-cta {
    color: var(--yellow); border: 2px solid var(--yellow);
    border-radius: 12px; padding: 1px 10px;
  }

  .countdown { position: absolute; left: 230px; top: 262px; font-family: "Roboto", sans-serif; font-weight: 700; }
  .countdown-days .value { font-size: 92px; line-height: 1; display: block; letter-spacing: -1px; }
  .countdown-days .rule { width: 245px; height: 2px; background: var(--yellow); margin-top: 8px; }
  .label { color: var(--yellow); text-transform: uppercase; }
  .countdown-days .label { font-size: 26px; display: block; margin-top: 8px; }
  .countdown-units { display: flex; gap: 6px; margin-top: 4px; }
  .unit .value { font-size: 50px; line-height: 1.05; display: block; }
  .unit .rule { height: 2px; background: var(--yellow); margin-top: 2px; }
  .unit .label { font-size: 18px; display: block; margin-top: 3px; }
  .unit-hours { width: 72px; }
  .unit-minutes { width: 77px; }
  .unit-seconds { width: 80px; }
  .unit-seconds .value { color: var(--yellow); }

  .divider { position: absolute; left: 0; top: 0; }

  .headline {
    position: absolute; left: 621px; top: 296px;
    font-family: "Roboto", sans-serif; font-weight: 700;
    text-transform: uppercase; line-height: 1.05;
  }
  .headline .line-sm { display: block; font-size: 44px; }
  .headline .accent { color: var(--orange); }
  .headline .line-lg { display: block; font-size: 56px; color: var(--yellow); margin-top: 2px; }

  .social { position: absolute; left: 35px; top: 682px; display: flex; gap: 12px; }
  .social span { width: 50px; height: 50px; border-radius: 50%; background: var(--yellow); }
  .social span.alt { background: var(--orange); }

  .subscribe { position: absolute; left: 632px; top: 685px; display: flex; height: 42px; }
  .subscribe input {
    width: 378px; border: 0; padding: 0 10px;
    font-family: "Raleway", sans-serif; font-weight: 600; font-size: 13px; color: var(--ink);
  }
  .subscribe input::placeholder { color: var(--ink); }
  .subscribe button {
    width: 153px; border: 0; background: var(--yellow); color: var(--white);
    font-family: "Roboto", sans-serif; font-weight: 700; font-size: 22px;
  }
</style>
</head>
<body>
<div class="page">
  <div class="hero-photo" role="img" aria-label="Overgrown railway track running into a dense green forest tunnel, darkened"></div>

  <div class="brand">
    <span class="brand-dot"></span>
    <span class="brand-name">EMBERMIST.COM</span>
  </div>

  <nav class="main-nav">
    <a href="#">Home</a>
    <a href="#">About</a>
    <a href="#">Contact</a>
    <a href="#" class="nav-cta">Buy Now</a>
  </nav>

  <div class="countdown">
    <div class="countdown-days">
      <span class="value">250</span>
      <div class="rule"></div>
      <span class="label">Days</span>
    </div>
    <div class="countdown-units">
      <div class="unit unit-hours"><span class="value">22</span><div class="rule"></div><span class="label">Hours</span></div>
      <div class="unit unit-minutes"><span class="value">45</span><div class="rule"></div><span class="label">Minutes</span></div>
      <div class="unit unit-seconds"><span class="value">15</span><div class="rule"></div><span class="label">Seconds</span></div>
    </div>
  </div>

  <svg class="divider" width="1200" height="800" aria-hidden="true">
    <line x1="615" y1="228" x2="536" y2="524" stroke="#ffc214" stroke-width="2"/>
  </svg>

  <h1 class="headline">
    <span class="line-sm">Fire prices on</span>
    <span class="line-sm">Premium <span class="accent">E-Juices</span></span>
    <span class="line-lg">Vaping soon</span>
  </h1>

  <div class="social" aria-label="Social links">
    <span></span><span></span><span class="alt"></span>
  </div>

  <form class="subscribe">
    <input type="email" placeholder="ENTER YOUR E-MAIL ADDRESS!">
    <button type="button">SUBSCRIBE</button>
  </form>
</div>
</body>
</html>
```